Attention grabbing 6x9 postcard

We are looking to have an attention grabbing post card that be sent out to homeowners from our roofing company Olum Roofing. the concept is that on the front it will say something like (STOP THE KNOCKING!
Tired of roofers knocking on your door? Contact us because we value your time as much as you value the roof over your head."
Olum Roofing
OlumRoofing.com
877.612.OLUM
info@olumroofing.com

Please feel free to come up with something very creative. Once we pick the final design we will provide the copy.

```html
<!DOCTYPE html>
<html lang="en">
<head>
<meta charset="utf-8">
<title>Olum Roofing – Postcard</title>
<link rel="stylesheet" href="https://fonts.googleapis.com/css2?family=Montserrat:wght@400;500;600;700;800;900&family=Roboto+Condensed:wght@700&display=swap">
<style>
  :root{
    --backdrop:#8b8b8b;
    --ink:#1c1c1c;
    --ink-soft:#2a2a2a;
    --gold:#e3b134;
    --gold-deep:#d19f22;
    --white:#ffffff;
    --paper:#f3f3f3;
    --rule:#c9c9c9;
  }
  *{box-sizing:border-box;margin:0;padding:0}
  html,body{width:1200px;height:900px;overflow:hidden}
  body{background:var(--backdrop);font-family:"Montserrat",sans-serif;position:relative}

  .card{position:absolute;width:645px;height:430px;overflow:hidden;box-shadow:0 4px 14px rgba(0,0,0,.25)}
  .card--front{left:277px;top:13px;background:linear-gradient(160deg,#232323,#141414)}
  .card--back{left:277px;top:457px;background:var(--gold)}

  .layer{position:absolute;inset:0}

  /* FRONT */
  .headline{position:absolute;left:178px;top:42px;width:292px;text-align:center;color:var(--white)}
  .headline__title{font-weight:900;font-size:24px;letter-spacing:.3px;line-height:1}
  .headline__sub{margin-top:8px;color:var(--gold);font-weight:800;font-size:14px;line-height:1.15;text-transform:uppercase}
  .headline__body{margin-top:8px;font-weight:500;font-size:11px;line-height:1.35}

  .brand-name{position:absolute;left:440px;top:292px;width:190px;text-align:center;color:var(--white);font-weight:600;font-size:17px;letter-spacing:4px;text-transform:uppercase}

  .contact-front{position:absolute;left:38px;top:350px;color:var(--white)}
  .contact-front__cta{color:var(--gold);font-weight:800;font-size:14px;letter-spacing:.5px;margin-bottom:3px}
  .contact-row{display:flex;align-items:center;gap:6px;font-size:13px;font-weight:400;line-height:1.35}
  .contact-row--strong{font-weight:700}
  .icon{width:12px;height:12px;flex:none}

  /* BACK */
  .section-label{position:absolute;left:0;height:20px;padding:0 34px 0 18px;background:var(--ink);color:var(--gold);font-weight:800;font-size:11.5px;line-height:20px;text-transform:uppercase;clip-path:polygon(0 0,100% 0,calc(100% - 14px) 100%,0 100%)}
  .copy{position:absolute;left:18px;color:var(--ink);font-size:8px;font-weight:500;line-height:1.35}

  .services{position:absolute;left:18px;top:86px;display:flex;gap:10px}
  .service{width:84px}
  .service__photo{width:84px;height:46px;border:2px solid var(--white)}
  .service__caption{margin-top:3px;font-family:"Roboto Condensed",sans-serif;font-weight:700;font-size:7.5px;line-height:1.1;text-transform:uppercase;color:var(--ink);text-align:center}

  .steps{position:absolute;left:18px;top:266px;width:300px;display:flex;flex-direction:column;gap:7px}
  .step{display:flex;align-items:center;gap:8px}
  .step__num{width:24px;height:22px;flex:none}
  .step__text{font-size:8px;font-weight:500;line-height:1.3;color:var(--ink)}

  .address-panel__name{position:absolute;left:430px;top:54px;color:var(--ink);font-weight:600;font-size:13px;letter-spacing:3px;text-transform:uppercase}
  .stamp-box{position:absolute;left:560px;top:16px;width:64px;height:60px;border:1px solid var(--rule)}
  .address-line{position:absolute;left:440px;width:185px;height:1px;background:var(--rule)}

  .vehicle{position:absolute;left:392px;top:226px;width:236px;height:150px;border-radius:40px 60px 30px 30px;background:radial-gradient(ellipse at 50% 40%,#b7bcc2,#6f747a 70%,#3b3e42)}

  .contact-back{position:absolute;display:flex;align-items:center;gap:5px;color:var(--white);font-size:11px;font-weight:400}
</style>
</head>
<body>

<!-- FRONT -->
<section class="card card--front" aria-label="Postcard front">
  <svg class="layer" viewBox="0 0 645 430" aria-hidden="false">
    <defs>
      <linearGradient id="tone-house" x1="0" y1="0" x2="0" y2="1">
        <stop offset="0" stop-color="#5f8a4f"/><stop offset=".55" stop-color="#b9bcc0"/><stop offset="1" stop-color="#8a8f93"/>
      </linearGradient>
      <linearGradient id="tone-roofline" x1="0" y1="0" x2="1" y2="1">
        <stop offset="0" stop-color="#c9d6e2"/><stop offset=".5" stop-color="#9a5a3e"/><stop offset="1" stop-color="#7a3b28"/>
      </linearGradient>
      <linearGradient id="tone-crew" x1="0" y1="0" x2="0" y2="1">
        <stop offset="0" stop-color="#4f7fc4"/><stop offset=".6" stop-color="#7c9ccf"/><stop offset="1" stop-color="#c98f5d"/>
      </linearGradient>
    </defs>

    <g stroke="var(--gold)" stroke-linecap="butt">
      <line x1="470" y1="0" x2="485" y2="40" stroke-width="12"/>
      <line x1="155" y1="0" x2="175" y2="180" stroke-width="12"/>
      <line x1="397" y1="216" x2="463" y2="154" stroke-width="14"/>
    </g>
    <rect x="214" y="248" width="32" height="14" fill="var(--gold)"/>

    <g class="hex hex--top">
      <polygon points="620,115 575,37.1 485,37.1 440,115 485,192.9 575,192.9" fill="var(--gold)"/>
      <polygon points="608,115 569,47.5 491,47.5 452,115 491,182.5 569,182.5" fill="var(--white)"/>
      <polygon role="img" aria-label="Photo of a two-storey white house with a new grey shingle roof" points="605,115 567.5,50 492.5,50 455,115 492.5,180 567.5,180" fill="url(#tone-house)"/>
    </g>
    <g class="hex hex--left">
      <polygon points="220,255 175,177.1 85,177.1 40,255 85,332.9 175,332.9" fill="var(--gold)"/>
      <polygon points="208,255 169,187.5 91,187.5 52,255 91,322.5 169,322.5" fill="var(--white)"/>
      <polygon role="img" aria-label="Photo of roofers laying tiles on a new brick house" points="205,255 167.5,190 92.5,190 55,255 92.5,320 167.5,320" fill="url(#tone-roofline)"/>
    </g>
    <g class="hex hex--middle">
      <polygon points="420,255 375,177.1 285,177.1 240,255 285,332.9 375,332.9" fill="var(--gold)"/>
      <polygon points="408,255 369,187.5 291,187.5 252,255 291,322.5 369,322.5" fill="var(--white)"/>
      <polygon role="img" aria-label="Photo of a roofing crew installing boards under a blue sky" points="405,255 367.5,190 292.5,190 255,255 292.5,320 367.5,320" fill="url(#tone-crew)"/>
    </g>
  </svg>

  <div class="headline">
    <h1 class="headline__title">STOP THE KNOCKING!</h1>
    <p class="headline__sub">Tired of roofers knocking<br>on your door?</p>
    <p class="headline__body">Contact us because we value<br>your time as much as you value<br>the roof over your head.</p>
  </div>

  <div class="brand-name">Olum Roofing</div>

  <div class="contact-front">
    <p class="contact-front__cta">CALL US TODAY</p>
    <p class="contact-row contact-row--strong">
      <svg class="icon" viewBox="0 0 12 12"><circle cx="6" cy="6" r="6" fill="var(--gold)"/><path d="M4 3.2l1.2 1.4-.6.8c.4.9 1 1.5 1.9 1.9l.8-.6L8.7 8 8 8.9C5.6 8.6 3.4 6.4 3.1 4z" fill="var(--ink)"/></svg>
      877.612.OLUM
    </p>
    <p class="contact-row">
      <svg class="icon" viewBox="0 0 12 12"><circle cx="6" cy="6" r="6" fill="var(--gold)"/><rect x="3" y="4" width="6" height="4.2" fill="none" stroke="var(--ink)" stroke-width=".9"/><path d="M3 4l3 2.4L9 4" fill="none" stroke="var(--ink)" stroke-width=".9"/></svg>
      info@olumroofing.com
    </p>
    <p class="contact-row">
      <svg class="icon" viewBox="0 0 12 12"><circle cx="6" cy="6" r="6" fill="var(--gold)"/><circle cx="6" cy="6" r="3.2" fill="none" stroke="var(--ink)" stroke-width=".8"/><path d="M2.8 6h6.4M6 2.8v6.4" stroke="var(--ink)" stroke-width=".7"/></svg>
      www.olumroofing.com
    </p>
  </div>
</section>

<!-- BACK -->
<section class="card card--back" aria-label="Postcard back">
  <svg class="layer" viewBox="0 0 645 430">
    <polygon points="412,0 645,0 645,345 392,345 392,48" fill="var(--ink)"/>
    <polygon points="424,0 645,0 645,335 402,335 402,52" fill="var(--paper)"/>
    <polygon points="0,398 330,398 356,372 645,372 645,430 0,430" fill="var(--ink)"/>
    <polygon points="356,366 645,366 645,372 356,372" fill="var(--gold-deep)"/>
    <polygon points="520,335 645,335 645,345 510,345" fill="var(--gold)"/>
  </svg>

  <h2 class="section-label" style="top:14px">Our Services</h2>
  <p class="copy" style="top:39px;width:370px">Olum Roofing offers an array of roofing solutions while providing professional, honest recommendations that address your specific needs. You can always count on us for exceptional service from the moment we meet. From inspection to installation, OLUM has you covered.</p>

  <div class="services">
    <figure class="service">
      <div class="service__photo" role="img" aria-label="Photo of a commercial building roof" style="background:linear-gradient(#a9c4dc,#6b6f78)"></div>
      <figcaption class="service__caption">Retail/Commercial<br>Roof Replacement</figcaption>
    </figure>
    <figure class="service">
      <div class="service__photo" role="img" aria-label="Photo of hail-damaged grey shingles" style="background:linear-gradient(135deg,#8d9196,#5e6267)"></div>
      <figcaption class="service__caption">Storm Damage<br>Roof Replacement</figcaption>
    </figure>
    <figure class="service">
      <div class="service__photo" role="img" aria-label="Photo of a new house under construction" style="background:linear-gradient(#5d86c8,#9a8a72)"></div>
      <figcaption class="service__caption">New<br>Construction</figcaption>
    </figure>
    <figure class="service">
      <div class="service__photo" role="img" aria-label="Photo of a roof covered with a blue repair tarp" style="background:linear-gradient(#7fa7cf,#4a7db8 55%,#8a8d90)"></div>
      <figcaption class="service__caption">Repairs<br>&amp; Restoration</figcaption>
    </figure>
  </div>

  <h2 class="section-label" style="top:162px">Our Mission</h2>
  <p class="copy" style="top:187px;width:365px">OLUM has always had one goal in mind: Create an experience that guarantees 100% satisfaction for each and every one of our clients. We believe in the power of transparency &amp; strive to make any roofing project as stress-free as possible. We use a simple process that begins with a free in-person consultation &amp; ends with a new roof backed by Olum Protection*.</p>

  <h2 class="section-label" style="top:240px">Olum Roofing Process</h2>
  <ol class="steps">
    <li class="step">
      <svg class="step__num" viewBox="0 0 24 22"><polygon points="23,11 17.5,1.5 6.5,1.5 1,11 6.5,20.5 17.5,20.5" fill="none" stroke="var(--ink)" stroke-width="2"/><text x="12" y="15.5" text-anchor="middle" font-family="Montserrat,sans-serif" font-weight="800" font-size="12" fill="var(--ink)">1</text></svg>
      <span class="step__text">Complimentary consultation to access your roofing needs<br>and review our honest recommendations.</span>
    </li>
    <li class="step">
      <svg class="step__num" viewBox="0 0 24 22"><polygon points="23,11 17.5,1.5 6.5,1.5 1,11 6.5,20.5 17.5,20.5" fill="none" stroke="var(--ink)" stroke-width="2"/><text x="12" y="15.5" text-anchor="middle" font-family="Montserrat,sans-serif" font-weight="800" font-size="12" fill="var(--ink)">2</text></svg>
      <span class="step__text">Our team of professionals replace, restore, or repair your<br>roof making the process as stress-free as possible.</span>
    </li>
    <li class="step">
      <svg class="step__num" viewBox="0 0 24 22"><polygon points="23,11 17.5,1.5 6.5,1.5 1,11 6.5,20.5 17.5,20.5" fill="none" stroke="var(--ink)" stroke-width="2"/><text x="12" y="15.5" text-anchor="middle" font-family="Montserrat,sans-serif" font-weight="800" font-size="12" fill="var(--ink)">3</text></svg>
      <span class="step__text">100% satisfaction, peace of mind &amp; continued professional<br>coverage backed by OLUM Protection*.</span>
    </li>
  </ol>

  <div class="stamp-box"></div>
  <div class="address-panel__name">Olum Roofing</div>
  <div class="address-line" style="top:120px"></div>
  <div class="address-line" style="top:148px"></div>
  <div class="address-line" style="top:176px"></div>

  <div class="vehicle" role="img" aria-label="Photo of a grey company pickup truck with yellow and black wrap"></div>

  <p class="contact-back" style="left:24px;top:406px">
    <svg class="icon" viewBox="0 0 12 12"><circle cx="6" cy="6" r="6" fill="var(--gold)"/><path d="M4 3.2l1.2 1.4-.6.8c.4.9 1 1.5 1.9 1.9l.8-.6L8.7 8 8 8.9C5.6 8.6 3.4 6.4 3.1 4z" fill="var(--ink)"/></svg>
    877.612.OLUM
  </p>
  <p class="contact-back" style="left:160px;top:406px">
    <svg class="icon" viewBox="0 0 12 12"><circle cx="6" cy="6" r="6" fill="var(--gold)"/><rect x="3" y="4" width="6" height="4.2" fill="none" stroke="var(--ink)" stroke-width=".9"/><path d="M3 4l3 2.4L9 4" fill="none" stroke="var(--ink)" stroke-width=".9"/></svg>
    info@olumroofing.com
  </p>
  <p class="contact-back" style="left:470px;top:392px">
    <svg class="icon" viewBox="0 0 12 12"><circle cx="6" cy="6" r="6" fill="var(--gold)"/><circle cx="6" cy="6" r="3.2" fill="none" stroke="var(--ink)" stroke-width=".8"/><path d="M2.8 6h6.4M6 2.8v6.4" stroke="var(--ink)" stroke-width=".7"/></svg>
    www.olumroofing.com
  </p>
</section>

</body>
</html>
```